Graphic lion print design with text

I like the gold effects in image 2 as described in my attached document, but i'm open to other suggestions. The desired image is image 1. This is a gift for a Leo friend. This is going to be printed and framed to be hung on the wall in a large frame, in landscape format. I like the idea of using different font styles to separate the statements.

Requirements
Must have
• I’m open to the suggestions about the font styles, but I want to separate the statements by using different font styles as shown in attached document.
Must be landscape format.
Small fonts preferred, as shown in the attached image.
Nice to have
• I like the gold effect in image 2 but other suggestions/colours welcome
Should not have
• Please don't stretch the picture so I can have a good resolution. Place the text on another black background template and then paste the picture beside to the text.

```html
<!DOCTYPE html>
<html lang="en">
<head>
<meta charset="UTF-8">
<title>Lion Blessing Print</title>
<link href="https://fonts.googleapis.com/css2?family=Marcellus&family=Marcellus+SC&family=Parisienne&display=swap" rel="stylesheet">
<style>
  :root {
    --page-bg: #f1f1f1;
    --print-black: #131210;
    --gold: #cdb978;
    --gold-pale: #eee4b6;
    --gold-deep: #8a7a3a;
    --band-dark: #050504;
  }
  * { margin: 0; padding: 0; box-sizing: border-box; }
  html, body {
    width: 1200px;
    height: 1000px;
    overflow: hidden;
    background: var(--page-bg);
  }
  .print {
    position: absolute;
    left: 50px;
    top: 112px;
    width: 1100px;
    height: 776px;
    background: var(--print-black);
    overflow: hidden;
  }
  .lion-art {
    position: absolute;
    left: 540px;
    top: 0;
    width: 560px;
    height: 776px;
    background:
      radial-gradient(ellipse 55% 48% at 62% 52%, rgba(176, 160, 70, 0.85) 0%, rgba(120, 110, 40, 0.6) 45%, rgba(60, 50, 20, 0.25) 75%, rgba(19, 18, 16, 0) 100%),
      radial-gradient(ellipse 40% 30% at 70% 18%, rgba(150, 110, 40, 0.6) 0%, rgba(19, 18, 16, 0) 100%);
  }
  .verse {
    position: absolute;
    left: 56px;
    white-space: nowrap;
    line-height: 1;
    font-family: "Marcellus", serif;
    color: var(--gold);
  }
  .verse--caps {
    font-family: "Marcellus SC", "Marcellus", serif;
    color: var(--gold-pale);
    letter-spacing: 1.5px;
  }
  .verse--script {
    font-family: "Parisienne", cursive;
    color: var(--gold-pale);
  }
  .divider {
    position: absolute;
    left: 50px;
    width: 520px;
    height: 10px;
    background: linear-gradient(90deg, rgba(5,5,4,0) 0%, rgba(5,5,4,0.9) 12%, rgba(5,5,4,0.9) 85%, rgba(5,5,4,0) 100%);
    box-shadow: 0 -3px 6px rgba(60, 55, 40, 0.35);
  }
</style>
</head>
<body>
  <main class="print">
    <div class="lion-art" role="img" aria-label="Golden-toned roaring lion in profile facing left, on black"></div>

    <p class="verse" style="top:32px; font-size:18px;">It doesn’t matter who or what may come against you,</p>
    <p class="verse verse--caps" style="top:65px; font-size:36px;">FOR GOD IS WITH YOU.</p>
    <p class="verse" style="top:110px; font-size:22px;">HE has made you more than a conqueror.</p>
    <div class="divider" style="top:138px;"></div>

    <p class="verse verse--script" style="top:172px; font-size:44px;">Almighty God</p>
    <p class="verse" style="top:226px; font-size:31px;">will come through for you</p>
    <p class="verse verse--caps" style="top:270px; font-size:34px;">WHEN YOU SEEK HIM</p>
    <p class="verse" style="top:314px; font-size:19px;">in your moments of trouble and unrest.</p>
    <div class="divider" style="top:345px;"></div>

    <p class="verse verse--caps" style="top:370px; font-size:34px;">MAY GOD</p>
    <p class="verse" style="top:414px; font-size:22px;">calm the restlessness of your mind and</p>
    <p class="verse" style="top:449px; font-size:27px;">still the thoughts that worry you.</p>
    <div class="divider" style="top:485px;"></div>

    <p class="verse verse--script" style="top:515px; font-size:41px;">Doors will open for you,</p>
    <p class="verse" style="top:575px; font-size:25px;">in the most unlikeliest of places.</p>
    <div class="divider" style="top:612px;"></div>

    <p class="verse" style="top:642px; font-size:28px;">When you go through deep waters,</p>
    <p class="verse verse--caps" style="top:679px; font-size:37px;">HE WILL BE WITH YOU.</p>
    <p class="verse" style="top:725px; font-size:16px;">Never will He leave you, Never will He forsake you. Amen.</p>
  </main>
</body>
</html>
```